Business Card Design Project

1. Show the company logo.
2. Only company email ID and website address to be shown (office@tikhayavolna.fm , www.tikhayavolna.fm).
3. Logo to be provided by us, 2 designs just in case. The logo is made with ' Tikhaya Volna' text, need to be edited so that it shows 'Yasnaya Afisha' instead .
4. Single sided business card, portrait or landscape is not a problem; back side to be filled with colors or a design that matches the logo the best.
5. Logo is to be embossed.
6. We're looking at an English and Russian version.
7. any other better idea is always welcomed.

```html
<!DOCTYPE html>
<html lang="en">
<head>
<meta charset="utf-8">
<title>Tikhaya Volna — Business Card</title>
<link rel="stylesheet" href="https://fonts.googleapis.com/css2?family=Mulish:wght@400;700;800&display=swap">
<style>
  :root {
    --page: #eceef1;
    --card-white: #ffffff;
    --brand-blue: #0a62a6;
    --ring-blue: #1f5aa0;
    --deep-navy: #0f2f6e;
    --halo-blue: #1570b6;
    --soft-blue: #9cbde3;
    --ghost-blue: #2b78b8;
    --white: #ffffff;
  }
  * { box-sizing: border-box; margin: 0; padding: 0; }
  html, body {
    width: 1052px;
    height: 1200px;
    overflow: hidden;
    background: var(--page);
    font-family: "Mulish", "Century Gothic", sans-serif;
  }
  .sheet {
    position: relative;
    width: 1052px;
    height: 1200px;
  }
  .card {
    position: absolute;
    left: 146px;
    width: 760px;
    height: 420px;
    overflow: hidden;
  }
  .card--front { top: 130px; background: var(--card-white); }
  .card--back  { top: 650px; background: var(--brand-blue); }
  .card__art {
    position: absolute;
    inset: 0;
    width: 760px;
    height: 420px;
  }
  .brand-name {
    position: absolute;
    color: var(--white);
    font-weight: 700;
    text-align: center;
    line-height: 1.15;
  }
  .card--front .brand-name {
    left: 45px; top: 170px; width: 310px; font-size: 34px;
  }
  .card--back .brand-name {
    left: 55px; top: 158px; width: 290px; font-size: 34px;
  }
  .contact {
    position: absolute;
    left: 418px;
    color: var(--white);
    font-weight: 800;
    font-size: 21px;
    letter-spacing: 0.2px;
  }
  .contact--web { top: 78px; }
  .contact--mail { top: 232px; }
  .tagline {
    position: absolute;
    left: 418px;
    top: 124px;
    color: var(--soft-blue);
    font-weight: 700;
    font-size: 30px;
    line-height: 1.1;
  }
  .ghost-name {
    position: absolute;
    left: 440px;
    top: 130px;
    color: var(--ghost-blue);
    font-weight: 800;
    font-size: 48px;
    line-height: 1.05;
  }
</style>
</head>
<body>
<main class="sheet">

  <section class="card card--front" aria-label="Business card, front">
    <svg class="card__art" viewBox="0 0 760 420" aria-hidden="true">
      <path fill="var(--brand-blue)"
            d="M260 40 H760 V300 H440 L415 326 L410 300 H364 A185 185 0 0 0 260 40 Z"/>
      <circle cx="200" cy="215" r="165" fill="var(--ring-blue)"/>
      <circle cx="200" cy="215" r="155" fill="var(--deep-navy)"/>
    </svg>
    <p class="brand-name">Tikhaya<br>Volna</p>
    <p class="contact contact--web">www.tikhayavolna.fm</p>
    <p class="tagline">Yasnaya<br>Afisha</p>
    <p class="contact contact--mail">office@tikhayavolna.fm</p>
  </section>

  <section class="card card--back" aria-label="Business card, back">
    <svg class="card__art" viewBox="0 0 760 420" aria-hidden="true">
      <circle cx="170" cy="200" r="300" fill="var(--halo-blue)"/>
      <circle cx="200" cy="200" r="150" fill="var(--ring-blue)"/>
      <circle cx="200" cy="200" r="140" fill="var(--deep-navy)"/>
    </svg>
    <p class="brand-name">Yasnaya<br>Afisha</p>
    <p class="ghost-name">Yasnaya<br>Afisha</p>
  </section>

</main>
</body>
</html>
```